UL Aesthetic improvement on full website

brightmeadowhq.com
We need someone to improve the current website brightmeadowhq.com
Some designed to fail to follow isntruction and deliver. please find attached summary latest design requirement, please follow and read each of the requirements carefully and submit max two versions only. The winner would have to deliver within 5 days

Sample reference : velorix.net/html/bluepark/#
(previous winner cant deliver)
*All of our wording and graphic content are updated, designer wouldn't involve in recreating any content.
Designer may use template or own material. delivery in html and implement on our WordPress server

please submit about us the project submission.
upon the winning, you have to maintain sub content / pages and submit the full site with your improved version of full websites including inner pages

Low design quality

Target Market(s)

general audience

Industry/Entity Type

social service

Number of Pages Required

5+ page

Requirements
Must have
• feeling and look similar to quindo dot com
Nice to have
• extend the same style to other pages

```html
<!DOCTYPE html>
<html lang="en">
<head>
<meta charset="utf-8">
<title>Bright Meadow</title>
<link href="https://fonts.googleapis.com/css2?family=Lato:wght@400;700;900&display=swap" rel="stylesheet">
<style>
:root{
  --coral:#f85a5e;
  --ink:#1f1f1f;
  --text:#4a4a4a;
  --grey:#f2f2f2;
  --dark:#1e1e20;
  --white:#ffffff;
}
*{margin:0;padding:0;box-sizing:border-box}
html,body{width:1200px;height:4485px;overflow:hidden}
body{position:relative;background:var(--white);font-family:'Lato',sans-serif;color:var(--text)}
.abs{position:absolute}
.bg-shapes{position:absolute;left:0;top:0;width:1200px;height:4485px}
.hero-photo{position:absolute;left:0;top:0;width:1200px;height:820px;background:linear-gradient(160deg,#3d4634 0%,#5b4a3c 40%,#6d5948 60%,#2f3a2c 100%)}
.hero-photo::after{content:"";position:absolute;inset:0;background:rgba(0,0,0,.25)}
.logo{position:absolute;display:flex;align-items:center;gap:10px}
.logo-dot{width:62px;height:62px;border-radius:50%;background:var(--coral)}
.logo-name{font-weight:900;font-size:15px;letter-spacing:1px;color:var(--white);line-height:1.1}
.nav{position:absolute;top:80px;left:0;width:1200px}
.nav a{position:absolute;color:var(--white);font-size:13px;font-weight:700;text-decoration:none;letter-spacing:.3px}
.nav .cta{background:var(--coral);left:991px;top:-10px;width:134px;height:38px;line-height:38px;text-align:center;border-radius:2px}
.hero-title{position:absolute;top:330px;width:1200px;text-align:center;color:var(--white);font-size:88px;font-weight:900;line-height:1}
.hero-sub{position:absolute;top:430px;width:1200px;text-align:center;color:var(--white);font-size:42px;font-weight:700;line-height:52px}
.h2{position:absolute;width:1200px;text-align:center;color:var(--ink);font-size:30px;font-weight:700}
.lead{position:absolute;width:1200px;text-align:center;font-size:15.5px;line-height:26px}
.card{position:absolute;width:330px;text-align:center;box-shadow:0 2px 12px rgba(0,0,0,.14);background:var(--white)}
.card .icon{width:64px;height:64px;margin:24px auto 0;border-radius:50%;background:#fbe2e3}
.card h3{color:var(--coral);font-size:24px;font-weight:700;margin-top:24px}
.card p{font-size:13.5px;line-height:26px;margin:12px 24px 0}
.btn-dark{display:inline-block;margin-top:20px;background:var(--ink);color:var(--white);font-size:15px;font-weight:700;width:117px;height:38px;line-height:38px;border-radius:2px}
.card.solid{background:var(--coral);color:var(--white);box-shadow:0 2px 10px rgba(0,0,0,.12)}
.card.solid .icon{background:rgba(255,255,255,.35);margin-top:34px;width:80px;height:80px}
.card.solid h3{color:var(--white);margin-top:20px}
.card.solid p{color:#ffe9ea}
.photo{position:absolute}
.about-title{position:absolute;left:615px;top:1692px;width:520px;color:var(--ink);font-size:31px;font-weight:700;line-height:44px}
.about-text{position:absolute;left:615px;top:1795px;width:520px;font-size:15.5px;line-height:33px}
.btn-coral{position:absolute;background:var(--coral);color:var(--white);font-weight:700;text-align:center;border-radius:2px}
.thumb{position:absolute;width:166px;height:167px}
.quote-mark{position:absolute;color:#b9b9b9;font-size:110px;font-weight:900;font-family:Georgia,serif;line-height:1}
.quote{position:absolute;left:615px;top:3070px;width:500px;font-size:20px;line-height:36.5px;color:#333}
.q-name{position:absolute;left:615px;top:3235px;color:var(--coral);font-size:16px;font-weight:700}
.dots{position:absolute;left:614px;top:3297px;display:flex;gap:12px}
.dots span{width:13px;height:13px;border-radius:50%;background:#333}
.dots span:first-child{background:var(--coral)}
.proj-title{position:absolute;left:77px;top:3693px;width:500px;color:var(--coral);font-size:28px;font-weight:700;line-height:36px}
.proj-text{position:absolute;left:77px;top:3770px;width:520px;font-size:15.5px;line-height:31px}
.foot{position:absolute;color:#ddd}
.foot h4{color:var(--white);font-size:16px;font-weight:700;margin-bottom:12px}
.foot li{list-style:none;font-size:13.5px;line-height:28px}
.foot-about{left:75px;top:4362px;width:320px;font-size:14px;line-height:26px;color:#ddd}
.email{display:flex;width:240px;height:36px;margin-top:4px}
.email span{flex:1;background:var(--white);color:#555;font-size:13px;line-height:36px;padding-left:12px}
.email b{width:41px;background:var(--coral);color:var(--white);font-size:14px;text-align:center;line-height:36px}
.copy{font-size:12.5px;line-height:20px;margin-top:48px}
.social{display:flex;gap:16px;margin-top:10px}
.social span{width:20px;height:20px;border-radius:50%;background:var(--white)}
</style>
</head>
<body>

<div class="hero-photo" role="img" aria-label="Group photo of smiling community volunteers outdoors raising their hands"></div>

<svg class="bg-shapes" viewBox="0 0 1200 4485" aria-hidden="true">
  <path fill="#ffffff" d="M0,812 C250,760 450,740 650,772 C850,805 1050,760 1200,690 L1200,830 L0,830 Z"/>
  <path fill="#f2f2f2" d="M0,1560 C250,1500 450,1560 700,1545 C950,1530 1100,1440 1200,1368 L1200,2160 C1000,2200 800,2130 600,2170 C400,2210 200,2230 0,2200 Z"/>
  <path fill="#f2f2f2" d="M0,2850 C250,2790 500,2790 700,2820 C900,2850 1050,2820 1200,2790 L1200,3420 C1000,3480 800,3400 600,3440 C400,3480 200,3460 0,3420 Z"/>
  <path fill="#1e1e20" d="M0,4260 C200,4170 400,4115 600,4112 C850,4110 1050,4150 1200,4220 L1200,4485 L0,4485 Z"/>
</svg>

<header>
  <div class="logo" style="left:75px;top:58px"><span class="logo-dot"></span><span class="logo-name">BRIGHT<br>MEADOW</span></div>
  <nav class="nav">
    <a style="left:405px">HOME</a>
    <a style="left:501px">SOCIAL IMPACT</a>
    <a style="left:660px">ABOUT US</a>
    <a style="left:784px">SERVICES</a>
    <a style="left:902px">BLOG</a>
    <a class="cta">CONTACT US</a>
  </nav>
  <h1 class="hero-title">Bright Meadow</h1>
  <p class="hero-sub">Sed ut perspiciatis unde omnis iste natus<br>sit voluptatem accusantium</p>
</header>

<section class="welcome">
  <h2 class="h2" style="top:883px">WELCOME TO OUR WEBSITE</h2>
  <p class="lead" style="top:942px">Lorem ipsum dolor sit amet, consectetur adipiscing elit. Curabitur egestas felis libero, ut tristique est maximus id.<br>Nulla tincidunt felis efficitur, interdum mi eu, auctor orci. Fusce tincidunt commodo velit in porttitor. Donec dapibus,<br>lacus quis molestie lobortis, mi elit luctus nisi, a maximus est ex vel lacus.</p>
  <div class="card" style="left:75px;top:1070px;height:298px"><div class="icon" role="img" aria-label="Hands holding a heart icon"></div><h3>Perspiciatis Unde</h3><p>Lorem ipsum dolor sit amet, consectetur adipiscing elit. Curabitur egestas felis libero, ut tristique es..</p><span class="btn-dark">Read More</span></div>
  <div class="card" style="left:435px;top:1070px;height:298px"><div class="icon" role="img" aria-label="Hands cradling a heart icon"></div><h3>Perspiciatis Unde</h3><p>Lorem ipsum dolor sit amet, consectetur adipiscing elit. Curabitur egestas felis libero, ut tristique es..</p><span class="btn-dark">Read More</span></div>
  <div class="card" style="left:796px;top:1070px;height:298px"><div class="icon" role="img" aria-label="Connected community people icon"></div><h3>Perspiciatis Unde</h3><p>Lorem ipsum dolor sit amet, consectetur adipiscing elit. Curabitur egestas felis libero, ut tristique es..</p><span class="btn-dark">Read More</span></div>
</section>

<section class="about">
  <div class="photo" style="left:75px;top:1650px;width:512px;height:423px;border-radius:6px;background:linear-gradient(135deg,#e9ecef 0%,#4fc0e0 45%,#39b3d8 70%,#d9dde0 100%)" role="img" aria-label="Cheering volunteers in blue T-shirts raising their fists"></div>
  <h2 class="about-title">NEMO ENIM IPSAM VOLUPTATEM QUIA VOLUPTAS SIT</h2>
  <p class="about-text">Lorem ipsum dolor sit amet, consectetur adipiscing elit. Curabitur egestas felis libero, ut tristique est maximus idtincidunt felis efficitur, interdum mi eu, auctor orci. Fusce tincidunt commodo velit in porttitor. Donec dapibus, lacus quis molestie lobortis, mi elit luctus nisi, a maximus est</p>
  <div class="btn-coral" style="left:615px;top:1981px;width:117px;height:38px;line-height:38px;font-size:15px">Read More</div>
</section>

<section class="services">
  <h2 class="h2" style="top:2258px">NEMO ENIM IPSAM</h2>
  <p class="lead" style="top:2316px">Lorem ipsum dolor sit amet, consectetur adipiscing elit. Curabitur egestas felis libero, ut tristique est maximus id.<br>Nulla tincidunt felis efficitur, interdum mi eu, auctor orci.</p>
  <div class="card solid" style="left:75px;top:2420px;height:291px"><div class="icon" role="img" aria-label="Volunteers with hearts icon"></div><h3>Perspiciatis Unde</h3><p>Lorem ipsum dolor sit amet, consectetur adipiscing elit. Curabitur egestas felis libero, ut tristique es..</p></div>
  <div class="card solid" style="left:435px;top:2420px;height:291px"><div class="icon" role="img" aria-label="Hand giving a coin icon"></div><h3>Perspiciatis Unde</h3><p>Lorem ipsum dolor sit amet, consectetur adipiscing elit. Curabitur egestas felis libero, ut tristique es..</p></div>
  <div class="card solid" style="left:796px;top:2420px;height:291px"><div class="icon" role="img" aria-label="Raised hands with heart icon"></div><h3>Perspiciatis Unde</h3><p>Lorem ipsum dolor sit amet, consectetur adipiscing elit. Curabitur egestas felis libero, ut tristique es..</p></div>
</section>

<section class="testimonials">
  <h2 class="h2" style="top:2882px">TESTIMONIALS</h2>
  <div class="thumb" style="left:164px;top:2979px;border:4px solid var(--coral);background:linear-gradient(160deg,#cfcfcf,#8a6d63 60%,#5a2f2f)" role="img" aria-label="Portrait of a young man with glasses"></div>
  <div class="thumb" style="left:357px;top:3092px;background:linear-gradient(160deg,#e6e6e6,#6b4a3a 55%,#c9a99a)" role="img" aria-label="Portrait of a smiling woman with dark hair"></div>
  <div class="thumb" style="left:164px;top:3200px;background:linear-gradient(160deg,#9aa3aa,#7b6659 50%,#2a2d3a)" role="img" aria-label="Portrait of a man in a suit and tie"></div>
  <div class="quote-mark" style="left:566px;top:3050px">&ldquo;</div>
  <p class="quote">Lorem ipsum dolor sit amet, consectetur &nbsp;adipiscing elit. Curabitur egestas felis libero, ut tristique est maximus id. Nulla tincidunt felis &nbsp;efficitur, interdum mi eused quia non numquam eius modi tempora.</p>
  <div class="q-name">NAME HEADING</div>
  <div class="quote-mark" style="left:1064px;top:3210px">&rdquo;</div>
  <div class="dots"><span></span><span></span><span></span><span></span></div>
</section>

<section class="projects">
  <h2 class="h2" style="top:3570px">OUR LATEST PROJECTS</h2>
  <h3 class="proj-title">Lorem ipsum dolor sit amet, adipiscing elit sed convallis sagittis</h3>
  <p class="proj-text">Curabitur egestas felis libero, ut tristique est maximus id incidunt felis efficitur, interdum mi eu, auctor orci. Fusce tincidunt commodo velit in porttitor. Donec dapibus, lacus quis molestie lobortis, mi elit luctus nisi, a maximus est ex vel lacus.</p>
  <div class="btn-coral" style="left:77px;top:3920px;width:165px;height:52px;line-height:52px;font-size:16px">READ MORE</div>
  <div class="photo" style="left:615px;top:3655px;width:512px;height:366px;background:linear-gradient(150deg,#2c3e6b 0%,#b23a3a 30%,#e7c34a 65%,#c06a4a 100%)" role="img" aria-label="Diverse group of smiling young people in front of a flag"></div>
</section>

<footer>
  <div class="logo" style="left:75px;top:4282px"><span class="logo-dot"></span><span class="logo-name">BRIGHT<br>MEADOW</span></div>
  <p class="foot foot-about">Sed vestibulum elit ex, convallis feugiat lacus consequat quis. Nulla sed ultricies donec et suscipit enim, at malesuada orci.</p>
  <div class="foot" style="left:442px;top:4240px"><h4>SITE MAP</h4><ul><li>Home</li><li>Social Impact</li><li>About Us</li><li>Services</li><li>Blog</li><li>Contact Us</li></ul></div>
  <div class="foot" style="left:655px;top:4240px"><h4>RESOURCES</h4><ul><li>Donec et suscipit</li><li>Enim at malesuada orc</li><li>Nam purus</li><li>Nulla convallis</li><li>Nulla et volutpat</li></ul></div>
  <div class="foot" style="left:885px;top:4240px"><h4>EMAIL SIGN UP</h4><div class="email"><span>Enter Email Address</span><b>GO</b></div><p class="copy">Copyright &copy; 2021. Company Name.<br>All Right Reserved</p><div class="social"><span></span><span></span><span></span><span></span><span></span></div></div>
</footer>

</body>
</html>
```